Harbor Nightclub

Nightclub flyer., digital single sided, for KV and PX. I included samples of some previous flyers we've used. Sample Info:
HARBOR
FRIDAYS
FRI MAY 1 2020
DJ VORTAN (club floor)
DJ RUZO & DJ TAV (residents on the lounge floor)
4217 Marlow Avenue Sacramento
www.harborvenuehall.example for list/VIP inquiries

Target Market(s)

Upscale top 40 crowd but want some cool and artsy like the examples included.

Font styles to use
Sans Serif

Requirements
Must have
• Harbor Logo
Nice to have
• Would be nice if the flyer can be incorporated later with DJ photos (sometimes we will add dj photos to pixagram etc). Would like a big city type of feel.
Should not have
• Nothing too sexual.

```html
<!DOCTYPE html>
<html lang="en">
<head>
<meta charset="utf-8">
<title>Harbor Nightclub – Friday May 1 2020</title>
<link rel="stylesheet" href="https://fonts.googleapis.com/css2?family=Arimo:wght@400;700&family=Josefin+Sans:wght@300;400&family=Oswald:wght@500&display=swap">
<style>
  :root {
    --stage: #2a2a2a;
    --ink-black: #050306;
    --club-red: #8a0f2e;
    --club-magenta: #c4134f;
    --hot-pink: #ff1f8a;
    --deep-purple: #2a0d3a;
    --headline-gold: #e4dd8a;
    --text-white: #f4f1f3;
    --text-soft: #d6d2d4;
  }
  * { margin: 0; padding: 0; box-sizing: border-box; }
  html, body { width: 1200px; height: 1200px; overflow: hidden; }
  body { background: var(--stage); position: relative; }

  .flyer {
    position: absolute; left: 119px; top: 0;
    width: 962px; height: 1200px;
    background: var(--ink-black);
    overflow: hidden;
    font-family: "Josefin Sans", sans-serif;
    color: var(--text-white);
  }
  .flyer__photo {
    position: absolute; inset: 0 0 300px 0;
    background:
      radial-gradient(ellipse at 75% 30%, var(--club-magenta) 0%, var(--club-red) 35%, transparent 70%),
      radial-gradient(ellipse at 20% 55%, #3b1a55 0%, transparent 60%),
      linear-gradient(180deg, #1a0610 0%, #4a0a20 40%, var(--ink-black) 100%);
  }
  .flyer__fade {
    position: absolute; left: 0; right: 0; top: 560px; height: 640px;
    background: linear-gradient(180deg, transparent 0%, rgba(5,3,6,.85) 45%, var(--ink-black) 70%);
  }
  .flyer__triangle { position: absolute; left: 0; top: 0; width: 962px; height: 900px; }

  .address {
    position: absolute; top: 70px; left: 0; right: 0; text-align: center;
    font-size: 29px; font-weight: 400; letter-spacing: 5px; color: var(--text-white);
    white-space: nowrap;
  }
  .date-box {
    position: absolute; left: 627px; top: 424px; width: 267px; height: 64px;
    border: 3px solid var(--text-white);
    display: flex; align-items: center; justify-content: center; gap: 11px;
    font-family: "Oswald", sans-serif; font-weight: 500; font-size: 33px; line-height: 1;
    color: var(--text-white); white-space: nowrap;
  }
  .date-box__part { white-space: nowrap; }
  .date-box__sep { width: 2px; height: 38px; background: var(--text-white); flex: none; }

  .lineup { position: absolute; left: 0; right: 0; top: 732px; text-align: center; }
  .lineup__name {
    font-family: "Arimo", sans-serif; font-weight: 700; color: var(--headline-gold);
    line-height: 1; letter-spacing: -1px; white-space: nowrap;
  }
  .lineup__name--headliner { font-size: 100px; }
  .lineup__name--residents { font-size: 84px; margin-top: 26px; }
  .lineup__note { font-size: 32px; font-weight: 300; color: var(--text-white); margin-top: 8px; }

  .brand {
    position: absolute; left: 72px; top: 1070px;
    display: flex; align-items: center; gap: 16px;
  }
  .brand__dot { width: 72px; height: 72px; border-radius: 50%; background: var(--text-soft); }
  .brand__name {
    font-family: "Josefin Sans", sans-serif; font-weight: 400; font-size: 42px;
    letter-spacing: 3px; color: var(--text-soft);
  }
  .contact { position: absolute; left: 557px; top: 1082px; white-space: nowrap; }
  .contact__url { font-family: "Arimo", sans-serif; font-weight: 700; font-size: 23px; color: var(--text-white); }
  .contact__note { font-size: 24px; font-weight: 300; color: var(--text-soft); margin-top: 4px; }
</style>
</head>
<body>
  <main class="flyer">
    <div class="flyer__photo" role="img" aria-label="Club photo: resident DJ at the decks with headphones, crowd and red stage lights behind"></div>
    <svg class="flyer__triangle" viewBox="0 0 962 900" aria-hidden="true">
      <polygon points="188,219 731,219 486,709" fill="var(--deep-purple)" opacity="0.55"/>
      <polygon points="188,219 731,219 720,240 205,240" fill="var(--hot-pink)"/>
      <polygon points="731,219 486,709 500,709 745,230" fill="var(--hot-pink)" opacity="0.85"/>
    </svg>
    <div class="flyer__fade"></div>

    <p class="address">4217 MARLOW AVENUE SACRAMENTO</p>

    <div class="date-box">
      <span class="date-box__part">FRI</span><span class="date-box__sep"></span>
      <span class="date-box__part">MAY 1</span><span class="date-box__sep"></span>
      <span class="date-box__part">2020</span>
    </div>

    <section class="lineup">
      <h1 class="lineup__name lineup__name--headliner">DJ VORTAN</h1>
      <p class="lineup__note">(club floor)</p>
      <h2 class="lineup__name lineup__name--residents">DJ RUZO &amp; DJ TAV</h2>
      <p class="lineup__note">(residents on the lounge floor)</p>
    </section>

    <div class="brand">
      <span class="brand__dot"></span>
      <span class="brand__name">HARBOR</span>
    </div>

    <div class="contact">
      <p class="contact__url">www.harborvenuehall.example</p>
      <p class="contact__note">for list/VIP inquiries</p>
    </div>
  </main>
</body>
</html>
```